PACKAGING DESIGN FOR ESSENTIAL OIL

The product is argan oil and I would be selling it in 30ml amber glass bottle.
I am looking for a design to put on the bottle. The brand name is BRUME DOUCE (Soft Mist translated in english). I would be using screen printing for the design on the glass bottle.
The bottle would be put in a carton box and I would need a design for that as well. I would like the carton box to be in gold colour (but you can propose a design with any other colour for the carton as well).
I am sending a picture with measurements of the glass bottle with its cap on it.
I am also sending the details I want to be included on the carton box.
I would like a design related to Morocco as the argan oil is from Morocco.
I have uploaded images that can inspire you all for my design.
I am sending you as well a link from findpix for Moroccan Mosaic:
https://www.findpix-example.test/search?q=argan+oil+brand&source=lnms&tbm=isch&sa=X&ei=aVZaUuKfFM7nrAeS7oGQAQ&ved=0CAcQ_AUoAQ&biw=1280&bih=658&dpr=1#q=moroccan+mosaic&tbm=isch&imgdii=_
Industry/Entity Type
Screen Printing
Requirements
Must have
- The Moroccan touch must be present in the design.
I would also like to have the brand name Brume Douce hot foil printed.
Nice to have
- A design of the argan tree would be nice as it shows exactly what we are selling.

```html
<!DOCTYPE html>
<html lang="fr">
<head>
<meta charset="utf-8">
<title>Brume Douce – front label</title>
<link rel="stylesheet" href="https://fonts.googleapis.com/css2?family=Cinzel:wght@400&family=Lato:wght@400&family=Poiret+One&display=swap">
<style>
  :root {
    --board-grey: #6d6d6d;
    --metallic-gold: #dd9118;
    --gold-light: #eaa93a;
    --gold-deep: #c27a0c;
    --print-white: #ffffff;
    --trim-magenta: #e0218a;
    --note-ink: #111111;
  }
  * { margin: 0; padding: 0; box-sizing: border-box; }
  html, body { width: 1200px; height: 1200px; overflow: hidden; }
  body {
    position: relative;
    background: var(--board-grey);
    font-family: "Lato", "Helvetica Neue", Arial, sans-serif;
  }
  .sheet-title {
    position: absolute; left: 83px; top: 52px;
    font-size: 19px; color: var(--note-ink);
  }
  .dimension {
    position: absolute; font-size: 19px; color: var(--note-ink); white-space: nowrap;
  }
  .dimension--width { left: 600px; top: 226px; transform: translateX(-50%); }
  .dimension--height { left: 950px; top: 595px; transform: translate(-50%, -50%) rotate(90deg); }

  .front-label {
    position: absolute; left: 385px; top: 302px; width: 430px; height: 598px;
    box-shadow: inset 0 0 0 2px var(--trim-magenta);
    text-align: center;
  }
  .brand-name {
    position: absolute; left: 0; right: 0; top: 22px;
    color: var(--metallic-gold);
    font-family: "Cinzel", "Trajan Pro", Georgia, serif;
    font-weight: 400; font-size: 100px; line-height: 104px; letter-spacing: 0;
  }
  .product-name {
    position: absolute; left: 0; right: 0; top: 256px;
    color: var(--print-white); font-size: 30px; line-height: 36px; letter-spacing: 0.5px;
  }
  .ornament {
    position: absolute; left: 153px; top: 347px; width: 124px; height: 114px;
  }
  .certification {
    position: absolute; left: 0; right: 0; top: 482px;
    color: var(--print-white); font-size: 32px; line-height: 38px;
  }
  .claim {
    position: absolute; left: 0; right: 0; top: 548px;
    color: var(--print-white); font-family: "Poiret One", "Arial Narrow", sans-serif;
    font-size: 21px; line-height: 28px; letter-spacing: 1px;
  }

  .colour-key { position: absolute; top: 1007px; left: 0; width: 100%; }
  .swatch { position: absolute; width: 81px; height: 81px; }
  .swatch--gold { left: 177px; background: var(--metallic-gold); }
  .swatch--white { left: 299px; background: var(--print-white); }
  .swatch--clear { left: 416px; border: 1.5px solid var(--print-white); }
  .swatch-name {
    position: absolute; top: 92px; width: 120px; margin-left: -20px;
    font-size: 18px; line-height: 19px; text-align: center; color: var(--note-ink);
  }
</style>
</head>
<body>
  <p class="sheet-title">front label</p>
  <p class="dimension dimension--width">25 mm</p>
  <p class="dimension dimension--height">35 mm</p>

  <section class="front-label">
    <h1 class="brand-name">BRUME<br>DOUCE</h1>
    <p class="product-name">HUILE D'ARGAN</p>
    <svg class="ornament" viewBox="0 0 124 114" role="img" aria-label="Moroccan arabesque medallion in metallic gold, hot foil">
      <defs>
        <radialGradient id="medallion-gold" cx="50%" cy="50%" r="55%">
          <stop offset="0%" stop-color="var(--gold-light)"/>
          <stop offset="70%" stop-color="var(--metallic-gold)"/>
          <stop offset="100%" stop-color="var(--gold-deep)"/>
        </radialGradient>
      </defs>
      <path d="M62 2 Q70 14 82 22 L114 50 Q122 57 114 64 L82 92 Q70 100 62 112 Q54 100 42 92 L10 64 Q2 57 10 50 L42 22 Q54 14 62 2 Z" fill="url(#medallion-gold)"/>
    </svg>
    <p class="certification">BIOLOGIQUE</p>
    <p class="claim">100% NATUREL</p>
  </section>

  <div class="colour-key">
    <div class="swatch swatch--gold"><p class="swatch-name">metalic<br>gold</p></div>
    <div class="swatch swatch--white"><p class="swatch-name">white</p></div>
    <div class="swatch swatch--clear"><p class="swatch-name">transparent<br>dont print</p></div>
  </div>
</body>
</html>
```